Mauspad für Hausarztpraxis
Zielgruppe
Hausarztpraxis - jung und modern
Aufgabenstellung
Mauspad- Gestaltung mit unserem Logo und Spruch. Farbe muss unser magenta mit sein, gern in Kombi mit Farben aus dem Bild an der Anmeldung ( das blau Kranich Bild)
Die Mauspad sind für uns gedacht am Arbeitsplatz, die aber von den Patienten gesehen werden.
https://www.wandlomax.de/de/bild/Blauer-Kranich-Pop-Art-Bild-Kunst-Urban-Contemporary-Modern-art/4820931?size=60x40&mediumId=13&aw_account=5820417396&aw_campaign=29017483615&utm_content=brand&aw_adgroup=&aw_creative=&aw_dev=m&aw_target=&gad_source=1&gclid=XqR7tLmP2vNs8KdWeYz4HbQc1FgTjUo9AiRx6MnVpEsLwZ3kDhCaYtBgNuJ5Fo_82XKLPQ7TYWVrHeZsJ4mBxD_CxE

```html
<!DOCTYPE html>
<html lang="de">
<head>
<meta charset="utf-8">
<title>Mauspad – Hausarztpraxis Dr. med. Marlene Osterwald</title>
<link href="https://fonts.googleapis.com/css2?family=Cinzel:wght@400;600;700&display=swap" rel="stylesheet">
<style>
  :root {
    --backdrop: #979797;
    --magenta: #c4195a;
    --slate: #545a5e;
    --paper: #ffffff;
    --violet: #6a3fc4;
    --lilac: #c9a8ee;
    --pink: #f04fb0;
  }
  * { margin: 0; padding: 0; box-sizing: border-box; }
  html, body {
    width: 706px;
    height: 1200px;
    overflow: hidden;
    background: var(--backdrop);
  }
  .canvas {
    position: relative;
    width: 706px;
    height: 1200px;
  }
  .mousepad {
    position: absolute;
    left: 112px;
    top: 68px;
    width: 482px;
    height: 482px;
    overflow: hidden;
    background: var(--paper);
  }
  .watercolour {
    position: absolute;
    inset: 0;
    background:
      radial-gradient(circle at 50% 36%, rgba(255,255,255,1) 0 28%, rgba(255,255,255,0) 46%),
      radial-gradient(ellipse at 90% 62%, rgba(106,63,196,.75) 0 14%, rgba(106,63,196,0) 32%),
      radial-gradient(ellipse at 10% 55%, rgba(106,63,196,.65) 0 12%, rgba(106,63,196,0) 30%),
      radial-gradient(ellipse at 20% 10%, rgba(240,79,176,.55) 0 10%, rgba(240,79,176,0) 28%),
      radial-gradient(ellipse at 80% 8%, rgba(240,79,176,.5) 0 10%, rgba(240,79,176,0) 26%),
      radial-gradient(ellipse at 30% 75%, rgba(240,79,176,.45) 0 10%, rgba(240,79,176,0) 28%),
      linear-gradient(180deg, var(--lilac) 0%, #efe3fb 50%, #d9c4f3 78%, #f6f0fc 100%);
  }
  .practice-mark {
    position: absolute;
    left: 127px;
    top: 58px;
    width: 220px;
    height: 220px;
    display: flex;
    flex-direction: column;
    align-items: center;
    justify-content: center;
    gap: 14px;
  }
  .practice-mark__dot {
    width: 64px;
    height: 64px;
    border-radius: 50%;
    background: var(--magenta);
  }
  .practice-mark__name {
    font-family: 'Cinzel', serif;
    font-weight: 700;
    font-size: 22px;
    color: var(--magenta);
    letter-spacing: 1px;
  }
  .signature {
    position: absolute;
    left: 0;
    right: 0;
    top: 396px;
    font-family: 'Cinzel', serif;
    text-align: center;
  }
  .signature__row {
    display: flex;
    align-items: center;
    justify-content: center;
    gap: 8px;
    padding: 0 26px;
  }
  .signature__rule {
    flex: 1;
    height: 2px;
    background: var(--slate);
  }
  .signature__kicker {
    font-size: 17px;
    font-weight: 600;
    letter-spacing: 4px;
    color: var(--slate);
  }
  .signature__name {
    font-size: 27px;
    font-weight: 700;
    color: var(--magenta);
    line-height: 1.1;
    margin: 2px 0 0;
    letter-spacing: 0.3px;
    white-space: nowrap;
  }
  .signature__claim {
    font-size: 11.5px;
    font-weight: 700;
    letter-spacing: 1.6px;
    color: var(--slate);
    white-space: nowrap;
  }
</style>
</head>
<body>
<main class="canvas">
  <section class="mousepad">
    <div class="watercolour" role="img" aria-label="Aquarell-Hintergrund in Violett, Flieder und Pink im Stil des Kranich-Bildes an der Anmeldung"></div>

    <div class="practice-mark">
      <span class="practice-mark__dot"></span>
      <span class="practice-mark__name">Osterwald</span>
    </div>

    <div class="signature">
      <div class="signature__row">
        <span class="signature__rule"></span>
        <span class="signature__kicker">HAUSARZTPRAXIS</span>
        <span class="signature__rule"></span>
      </div>
      <p class="signature__name">DR. MED. MARLENE OSTERWALD</p>
      <div class="signature__row">
        <span class="signature__rule"></span>
        <span class="signature__claim">MIT HERZ UND VERSTAND FÜR SIE DA</span>
        <span class="signature__rule"></span>
      </div>
    </div>
  </section>
</main>
</body>
</html>
```